Website Home Page for Women's Health Medical Office

Redesign existing homepage for website using existing logo. Current website location is www.lumawomenscare.com. Please give it a modern, streamlined, playful feel.

Please give it a feminine feel and make it bright and cheerful using logo colors.

Target Market(s)

Women between the ages of 25-45

Industry/Entity Type

Medical Office

Coding

Coded - Design and coding required

Number of Pages Required

1 page

Font styles to use
Sans Serif
Other font styles liked:
• SEGOI UI script for text and GIL SANS for bold (or their equivilent)

Colors
E54698
E96AAD
F1A4CE
F9D9EA
FCEFF6

Requirements
Must have
• Existing logo. Logo Colors. Feminine, cheerful, simple design. all relevant contact information
Nice to have
• clean lines and streamlined look
Should not have
• Cluttered

```html
<!DOCTYPE html>
<html lang="en">
<head>
<meta charset="utf-8">
<title>Luma Women's Care – Home</title>
<link href="https://fonts.googleapis.com/css2?family=Outfit:wght@400;500;600;700&family=Open+Sans:wght@400;600&display=swap" rel="stylesheet">
<style>
:root{
  --pink:#F7068D;
  --pink-mid:#E96AAD;
  --pink-soft:#F1A4CE;
  --pink-light:#F9D9EA;
  --pink-pale:#FCEFF6;
  --ink:#1E1E1E;
  --text:#333;
  --dark:#333436;
  --white:#fff;
  --photo-a:#d8c7cf;
  --photo-b:#b99aa8;
}
*{box-sizing:border-box;margin:0;padding:0}
html,body{width:1200px;height:4092px;overflow:hidden}
body{position:relative;background:var(--white);font-family:"Open Sans",sans-serif;color:var(--text)}
.abs{position:absolute}
h1,h2,h3,.heading{font-family:"Outfit",sans-serif;font-weight:500;color:var(--pink)}
.photo{background:linear-gradient(160deg,var(--photo-a),var(--photo-b))}

/* header */
.site-header{position:absolute;left:0;top:0;width:1200px;height:127px;background:var(--white)}
.brand{position:absolute;left:76px;top:40px;display:flex;align-items:center;gap:12px}
.brand-dot{width:18px;height:18px;border-radius:50%;background:var(--pink)}
.brand-name{font-family:"Outfit",sans-serif;font-weight:700;font-size:30px;color:var(--ink)}
.contact-item{position:absolute;top:42px;display:flex;gap:8px;font-size:11px;line-height:15px;color:var(--ink)}
.contact-item small{display:block;color:var(--pink);font-size:10.5px}
.contact-item svg{flex:none;margin-top:2px}

/* nav */
.main-nav{position:absolute;left:0;top:127px;width:1200px;height:73px;background:var(--pink)}
.nav-link{position:absolute;top:25px;font-family:"Outfit",sans-serif;font-size:16px;color:var(--white)}
.btn-book{position:absolute;left:850px;top:17px;width:210px;height:40px;border-radius:10px;background:var(--white);color:var(--pink);font-family:"Outfit",sans-serif;font-size:16px;font-weight:500;display:flex;align-items:center;justify-content:center}

/* hero */
.hero-title{position:absolute;left:135px;top:308px;font-size:38px;line-height:54px;width:590px;white-space:nowrap}
.hero-lead{position:absolute;left:138px;top:442px;font-size:19px;line-height:28px;color:var(--ink);width:420px}
.hero-photo{position:absolute;left:734px;top:250px;width:331px;height:433px;border-radius:165px 165px 110px 110px}

/* intro */
.intro-frame{position:absolute;left:185px;top:770px;width:323px;height:417px;border:1.5px solid var(--pink);border-radius:160px}
.intro-photo{position:absolute;left:210px;top:782px;width:273px;height:375px;border-radius:137px}
.intro-title{position:absolute;left:623px;top:780px;font-size:30px;line-height:41px}
.intro-copy{position:absolute;left:619px;top:883px;width:442px;font-size:13.5px;line-height:20px;color:var(--ink)}
.intro-copy p+p{margin-top:20px}

/* banner */
.cta-banner{position:absolute;left:138px;top:1280px;width:922px;height:255px;border-radius:30px 30px 0 0;background:linear-gradient(180deg,var(--pink-light),var(--white))}
.cta-kicker{position:absolute;left:92px;top:55px;font-family:"Outfit",sans-serif;font-size:20px;color:var(--pink)}
.cta-title{position:absolute;left:92px;top:86px;font-family:"Outfit",sans-serif;font-size:30px;color:var(--ink)}
.cta-text{position:absolute;left:92px;top:152px;font-family:"Outfit",sans-serif;font-size:19px;line-height:28px;color:var(--ink)}
.cta-text span{color:var(--pink)}
.cta-illustration{position:absolute;left:545px;top:-10px;width:385px;height:265px;border-radius:40px;background:linear-gradient(160deg,var(--pink-light),var(--pink-pale))}

/* services */
.services-title{position:absolute;left:0;top:1673px;width:1200px;text-align:center;font-size:30px}
.services-sub{position:absolute;left:0;top:1720px;width:1200px;text-align:center;font-family:"Outfit",sans-serif;font-size:16px;color:var(--ink)}
.service{position:absolute;width:520px;height:270px}
.service-photo{position:absolute;left:0;top:0;width:186px;height:258px;border-radius:50%;border:1.5px solid var(--pink)}
.service h3{position:absolute;left:212px;top:20px;font-size:28px;line-height:36px;width:280px}
.service p{position:absolute;left:212px;font-size:12.5px;line-height:18.4px;color:var(--ink);width:212px}
.btn-more{position:absolute;left:212px;height:27px;padding:0 14px;border-radius:6px;background:var(--pink);color:var(--white);font-family:"Outfit",sans-serif;font-size:14px;font-weight:500;display:flex;align-items:center;letter-spacing:.5px}

/* specialist */
.specialist-bg{position:absolute;left:0;top:2480px;width:1200px;height:590px;background:linear-gradient(180deg,var(--white),var(--pink-light))}
.specialist-title{position:absolute;left:143px;top:2575px;font-size:30px}
.specialist-copy{position:absolute;left:139px;top:2643px;width:478px;font-size:13.5px;line-height:20px;color:var(--ink)}
.specialist-copy p+p{margin-top:20px}
.specialist-photo{position:absolute;left:712px;top:2552px;width:348px;height:443px;border-radius:170px 170px 130px 130px;border:1.5px solid var(--pink)}

/* contact */
.contact-card{position:absolute;left:78px;top:3175px;width:562px;height:635px;background:var(--pink-light);border-radius:110px 20px 40px 40px}
.contact-title{position:absolute;left:0;top:55px;width:100%;text-align:center;font-size:30px}
.field{position:absolute;height:46px;background:var(--white);border-radius:4px;font-size:12.5px;color:var(--ink);padding:16px 16px}
.field span{color:var(--pink)}
.field-label{position:absolute;font-size:12.5px;color:var(--ink)}
.field-label span{color:var(--pink)}
.btn-submit{position:absolute;left:58px;top:538px;width:130px;height:32px;border-radius:16px;background:var(--pink);color:var(--white);font-family:"Outfit",sans-serif;font-size:14px;font-weight:500;display:flex;align-items:center;justify-content:center}
.contact-brand{position:absolute;left:730px;top:3218px;display:flex;align-items:center;gap:10px}
.contact-brand .brand-name{font-size:26px}
.contact-line{position:absolute;left:733px;display:flex;gap:12px;font-size:15px;line-height:21px;color:var(--ink)}
.contact-line svg{flex:none;margin-top:3px}

/* footer */
.site-footer{position:absolute;left:0;top:3865px;width:1200px;height:184px;background:var(--dark)}
.footer-nav{position:absolute;top:44px;font-family:"Outfit",sans-serif;font-size:16px;color:var(--white)}
.plans{position:absolute;left:150px;top:95px;width:900px;text-align:center;font-size:8.5px;line-height:13px;color:var(--white)}
.plans span{white-space:nowrap;margin:0 5px}
.plans span::before{content:"✓ ";font-weight:600}
.copyright{position:absolute;left:0;top:4049px;width:1200px;height:43px;background:var(--pink);color:var(--white);font-size:12px;display:flex;align-items:center;justify-content:center}
</style>
</head>
<body>

<header class="site-header">
  <div class="brand"><span class="brand-dot"></span><span class="brand-name">Luma Women's Care</span></div>
  <div class="contact-item" style="left:577px">
    <svg width="16" height="16" viewBox="0 0 24 24" fill="none" stroke="#F7068D" stroke-width="2"><path d="M22 16.9v3a2 2 0 0 1-2.2 2 19.8 19.8 0 0 1-8.6-3.1 19.5 19.5 0 0 1-6-6A19.8 19.8 0 0 1 2.1 4.2 2 2 0 0 1 4.1 2h3a2 2 0 0 1 2 1.7c.1.9.4 1.8.7 2.7a2 2 0 0 1-.5 2.1L8 9.8a16 16 0 0 0 6 6l1.3-1.3a2 2 0 0 1 2.1-.4c.9.3 1.8.6 2.7.7a2 2 0 0 1 1.9 2z"/></svg>
    <div><small>Have Any Questions?</small>(555) 014-2290</div>
  </div>
  <div class="contact-item" style="left:737px">
    <svg width="16" height="16" viewBox="0 0 24 24" fill="none" stroke="#F7068D" stroke-width="2"><rect x="2" y="4" width="20" height="16" rx="2"/><path d="M2 6l10 7 10-7"/></svg>
    <div><small>Email us</small>admin@lumawomenscare.com</div>
  </div>
  <div class="contact-item" style="left:936px">
    <svg width="16" height="16" viewBox="0 0 24 24" fill="none" stroke="#F7068D" stroke-width="2"><path d="M12 22s7-6.5 7-12a7 7 0 0 0-14 0c0 5.5 7 12 7 12z"/><circle cx="12" cy="10" r="2.5"/></svg>
    <div><small>Our Location</small>4120 Maple Grove Avenue, Suite<br>210, Lakeview, CA 90210</div>
  </div>
</header>

<nav class="main-nav">
  <span class="nav-link" style="left:76px">Home</span>
  <span class="nav-link" style="left:155px">Services ⌄</span>
  <span class="nav-link" style="left:263px">Resources ⌄</span>
  <span class="nav-link" style="left:393px">About Us</span>
  <span class="nav-link" style="left:498px">Contact us</span>
  <span class="btn-book">BOOK APPOINTMENT</span>
</nav>

<svg class="abs" style="left:0;top:200px" width="1200" height="523" viewBox="0 0 1200 523" aria-hidden="true">
  <path d="M0 0H1200V523H0z" fill="#FCEFF6"/>
  <path d="M475 0H1200V448C1100 450 1010 440 930 410 810 370 720 300 650 190 600 110 530 50 475 0z" fill="#F9D9EA"/>
  <path d="M0 523C100 470 240 430 420 420 600 410 760 440 900 470 1020 495 1110 500 1200 490V523z" fill="#fff"/>
  <path d="M1105 112a16 16 0 0 0 32 -16" fill="none" stroke="#F7068D" stroke-width="6" stroke-linecap="round"/>
  <path d="M118 360a16 16 0 0 1 -30 -20" fill="none" stroke="#F7068D" stroke-width="6" stroke-linecap="round"/>
</svg>
<h1 class="hero-title">Welcome to Luma Women's<br>Care, Lakeview, CA</h1>
<p class="hero-lead">Lorem ipsum dolor sit amet, consectetur adipiscing elit. Scelerisque viverra nullam.</p>
<div class="hero-photo photo" role="img" aria-label="Photo of a nurse taking a smiling patient's blood pressure"></div>

<div class="intro-frame"></div>
<div class="intro-photo photo" role="img" aria-label="Portrait photo of a smiling doctor in navy scrubs"></div>
<h2 class="intro-title">Serving Lakeview Springs<br>Medical Center</h2>
<div class="intro-copy">
  <p>At Luma Women's Care in Lakeview, California, we believe better health starts when the patient is educated. For this reason, we take time to listen to our patients concerns, explain each option available, and to answer any questions our patients may have so that they can make informed decisions. At Luma Women's Care, our providers tailor every procedure performed and treatment option recommended to meet the specific needs of our patients. We remain up-to-date on the latest technology and practice guidelines for women's health.</p>
  <p>Our medical providers will take time to give you the personalized health care you deserve. This includes taking time to listen to you and screening you for problems to help ensure that any health issues are diagnosed and treated as early as possible.</p>
</div>

<section class="cta-banner">
  <div class="cta-kicker">Better Health Starts Here!</div>
  <div class="cta-title">Now Accepting New Patients</div>
  <div class="cta-text"><span>Click Here</span> for an Appointment<br>or Call Us At <span>(555) 014-2290</span></div>
  <div class="cta-illustration" role="img" aria-label="Line illustration of a doctor with a clipboard talking to a woman patient"></div>
</section>

<h2 class="services-title">How we can help you?</h2>
<div class="services-sub">Health Services Offered</div>

<article class="service" style="left:138px;top:1796px">
  <div class="service-photo photo" role="img" aria-label="Photo of an ultrasound appointment with a pregnant patient"></div>
  <h3>Pregnancy Care</h3>
  <p style="top:52px">Receiving regular care in pregnancy is important for the health of both you and your baby. Our obstetricians work with you every step of the way during your pregnancy and delivery to make sure your individual needs are met and co ensure this special journey is a memorable one.</p>
  <span class="btn-more" style="top:237px">LEARN MORE</span>
</article>
<article class="service" style="left:638px;top:1793px">
  <div class="service-photo photo" role="img" aria-label="Photo of hands holding an ultrasound print"></div>
  <h3>Birth Control</h3>
  <p style="top:52px">Our gynecologists are knowledgeable on all forms of birth control including the IUD, Nexplanon, vaginal ringinsertion, birth control pills, and more! We would love to work with you to determine the best option for you and your lifestyle.</p>
  <span class="btn-more" style="top:237px">LEARN MORE</span>
</article>
<article class="service" style="left:138px;top:2125px">
  <div class="service-photo photo" role="img" aria-label="Photo of a provider examining a patient"></div>
  <h3>Well Woman<br>Exams</h3>
  <p style="top:93px">Our providers will help you to stay healthy by performing a physical exam on you annually. We will screen you for multiple health conditions that may pose a risk to you. This includes screening you for cancerous conditions of the breast, ovaries and cervix.</p>
  <span class="btn-more" style="top:248px">LEARN MORE</span>
</article>
<article class="service" style="left:638px;top:2127px">
  <div class="service-photo photo" role="img" aria-label="Photo of a doctor checking a pregnant patient"></div>
  <h3>Woman's Health</h3>
  <p style="top:52px">Whether you are dealing with painful or irregular periods, fibroids, or other women's health i ssues, we can help. We offer a variety of the most up-to-date treatment options to help you regain your lifestyle.</p>
  <span class="btn-more" style="top:195px">LEARN MORE</span>
</article>

<div class="specialist-bg"></div>
<h2 class="specialist-title">Your OB/GYN Specialist</h2>
<div class="specialist-copy">
  <p>Luma Women's Care offers you the best care possible in a personalized setting. We are currently accepting patients. Call our office now to make an appointment.</p>
  <p>Luma Women's Care (located near Lakeview Springs Hospital in Lakeview, CA) is a medical office that specializes in Christ-centered healthcare for women of all ages. Our team of exclusively female providers have years of experience taking care of women with a variety of pregnancy and gynecology concerns.</p>
  <p>Whether you need a routine examination, help during your pregnancy, have questions on birth control, or another female concern, we offer the best care possible for our patients. That is why better health starts here.</p>
  <p>Our office provides you with an environment where you can feel comfortable and where you know you will be in good hands. Our providers are leaders women's health. Dr. Marlow is a board certified obstetrician and gynecologist. Dr. Castell is a board eligible obstetrician and gynecologist.</p>
</div>
<div class="specialist-photo photo" role="img" aria-label="Photo of a smiling provider holding a newborn baby"></div>
<svg class="abs" style="left:712px;top:2585px" width="60" height="40" aria-hidden="true"><path d="M8 6a20 20 0 0 0 40 4" fill="none" stroke="#F7068D" stroke-width="7" stroke-linecap="round"/></svg>

<section class="contact-card">
  <h2 class="contact-title">Contact us</h2>
  <div class="field" style="left:62px;top:117px;width:218px">First Name</div>
  <div class="field" style="left:294px;top:117px;width:210px">Last Name</div>
  <div class="field" style="left:62px;top:183px;width:442px">Email Address<span>*</span></div>
  <div class="field" style="left:62px;top:250px;width:442px">Phone Number<span>*</span></div>
  <div class="field-label" style="left:62px;top:323px">Type of request<span>*</span></div>
  <div class="field" style="left:62px;top:348px;width:442px;color:#666;padding-left:22px">-Select-
    <svg class="abs" style="right:38px;top:16px" width="20" height="12" viewBox="0 0 20 12" fill="none" stroke="#666" stroke-width="1.5"><path d="M1 1l9 9 9-9"/></svg>
  </div>
  <div class="field" style="left:62px;top:418px;width:442px;height:95px;padding-left:14px">Message<span>*</span></div>
  <span class="btn-submit">SUBMIT</span>
</section>

<div class="contact-brand"><span class="brand-dot"></span><span class="brand-name">Luma Women's Care</span></div>
<div class="contact-line" style="top:3322px">
  <svg width="16" height="16" viewBox="0 0 24 24" fill="none" stroke="#F7068D" stroke-width="2"><path d="M12 22s7-6.5 7-12a7 7 0 0 0-14 0c0 5.5 7 12 7 12z"/><circle cx="12" cy="10" r="2.5"/></svg>
  <span>4120 Maple Grove Avenue, Suite<br>210, Lakeview, CA 90210</span>
</div>
<div class="contact-line" style="top:3384px">
  <svg width="16" height="16" viewBox="0 0 24 24" fill="none" stroke="#F7068D" stroke-width="2"><path d="M22 16.9v3a2 2 0 0 1-2.2 2 19.8 19.8 0 0 1-8.6-3.1 19.5 19.5 0 0 1-6-6A19.8 19.8 0 0 1 2.1 4.2 2 2 0 0 1 4.1 2h3a2 2 0 0 1 2 1.7c.1.9.4 1.8.7 2.7a2 2 0 0 1-.5 2.1L8 9.8a16 16 0 0 0 6 6l1.3-1.3a2 2 0 0 1 2.1-.4c.9.3 1.8.6 2.7.7a2 2 0 0 1 1.9 2z"/></svg>
  <span>(555) 014-2290</span>
</div>
<div class="contact-line" style="top:3423px">
  <svg width="16" height="16" viewBox="0 0 24 24" fill="none" stroke="#F7068D" stroke-width="2"><rect x="6" y="2" width="12" height="20" rx="1"/><path d="M9 7h6M9 11h6M9 15h6"/></svg>
  <span>(555) 014-2291</span>
</div>
<div class="contact-line" style="top:3464px">
  <svg width="16" height="16" viewBox="0 0 24 24" fill="none" stroke="#F7068D" stroke-width="2"><rect x="2" y="4" width="20" height="16" rx="2"/><path d="M2 6l10 7 10-7"/></svg>
  <span>admin@lumawomenscare.com</span>
</div>

<footer class="site-footer">
  <span class="footer-nav" style="left:267px">Home</span>
  <span class="footer-nav" style="left:347px">About us</span>
  <span class="footer-nav" style="left:468px">News</span>
  <span class="footer-nav" style="left:561px">Patient Resources</span>
  <span class="footer-nav" style="left:744px">Privacy Policy</span>
  <span class="footer-nav" style="left:903px">Contact us</span>
  <div class="plans">
    <span>Brightpath</span>|<span>Valley Direct</span>|<span>Careline North</span>|<span>Careline East</span>|<span>Senior Circle</span>|<span>Harbor Medical Group</span>|<span>Service Plan Prime</span>|<span>Meadow Physicians</span>|<br>
    <span>Northstar Open Select</span>|<span>Summit Select</span>|<span>Clearwater Shield</span>|<span>Keystone</span>|<span>Keystone Local Plus</span>|<span>Veteran Family Plan</span>|<span>EBS Group</span>|<span>Federal Care Assoc.</span>|<span>WellNet</span>|<span>Horizon Care</span>|<br>
    <span>Steel Trades Trust Fund</span>|<span>Builders Health &amp; Welfare Fund</span>|<span>Postal Workers Plan</span>|<span>Machine Operators</span>|<span>Metal Trades Union</span>|<span>Service Plan Select</span>|<span>Unity Health Plans</span>|<br>
    <span>Retail Workers Plan</span>|<span>Benefit Partners</span>|<span>Careline South</span>
  </div>
</footer>
<div class="copyright">2022 ©Luma Women's Care</div>

</body>
</html>
```